New business card for civil engineering company - "Keystone Audit"

We need a business card designed for our new structural engineering company.

The company name is "Keystone Audit" logo files attached.

We would like the following:
* Two-sided card
* Simple design

Information to be placed on the card:
Name - Marcus Dellow
Job Title - Director / Structural Engineer
Credentials - BEng(Hons), CPEng, CMengNZ, IntPE(NZ)
Email - marcus.dellow@keystoneaudit.co.nz
mobile - 0219364058
website - www.keystoneaudit.co.nz

```html
<!DOCTYPE html>
<html lang="en">
<head>
<meta charset="utf-8">
<title>Keystone Audit – Business Card</title>
<link href="https://fonts.googleapis.com/css2?family=Open+Sans:wght@400;600;700&display=swap" rel="stylesheet">
<style>
  :root {
    --backdrop: #0b0b0b;
    --paper: #f6f6f6;
    --charcoal: #2f2f30;
    --brand-blue: #3a7fc9;
    --blue-light: #a9d0ee;
    --blue-mid: #6aaee0;
    --blue-deep: #3f86c8;
    --text-grey: #6a6a6a;
    --text-white: #f2f2f2;
  }
  * { box-sizing: border-box; margin: 0; padding: 0; }
  html, body {
    width: 1200px; height: 856px; overflow: hidden;
    background: var(--backdrop);
    font-family: "Open Sans", Arial, sans-serif;
  }
  .canvas {
    width: 1200px; height: 856px;
    display: flex; align-items: center; justify-content: center; gap: 40px;
  }
  .card {
    position: relative; width: 560px; height: 320px; overflow: hidden;
  }
  /* Front */
  .card-front { background: var(--paper); }
  .front-details {
    position: absolute; left: 28px; top: 26px; z-index: 2;
    white-space: nowrap;
  }
  .person-name { color: var(--brand-blue); font-weight: 700; font-size: 23px; line-height: 1.1; }
  .person-role, .person-credentials { color: var(--text-grey); font-size: 14px; line-height: 1.35; }
  .person-role { margin-top: 4px; }
  .contact-list {
    position: absolute; left: 28px; bottom: 30px; list-style: none;
    color: var(--text-grey); font-size: 13px; z-index: 2;
  }
  .contact-list li { display: flex; align-items: center; gap: 9px; line-height: 1.6; white-space: nowrap; }
  .contact-list svg { width: 14px; height: 14px; flex: none; }
  .accent-band {
    position: absolute; left: 300px; top: 104px; width: 64px; bottom: 0;
    background: linear-gradient(180deg, var(--blue-light) 0%, var(--blue-mid) 60%, var(--blue-deep) 100%);
  }
  .front-panel {
    position: absolute; right: 0; top: 0; width: 196px; height: 100%;
    background: var(--charcoal);
  }
  .panel-name {
    position: absolute; left: 0; right: 0; top: 128px; text-align: center;
    color: var(--text-white); font-weight: 600; font-size: 19px; letter-spacing: 0.04em;
  }
  .panel-url {
    position: absolute; left: 0; right: 0; bottom: 30px; text-align: center;
    color: var(--text-white); font-size: 12px;
  }
  /* Back */
  .card-back { background: var(--charcoal); display: flex; align-items: center; justify-content: center; }
  .back-brand { display: flex; align-items: center; gap: 12px; }
  .brand-square { width: 18px; height: 18px; background: var(--brand-blue); }
  .back-name { color: var(--text-white); font-weight: 600; font-size: 32px; letter-spacing: 0.05em; }
</style>
</head>
<body>
<main class="canvas">
  <section class="card card-front" aria-label="Card front">
    <div class="accent-band" role="img" aria-label="Blue faceted decorative shape"></div>
    <div class="front-panel">
      <p class="panel-name">Keystone Audit</p>
      <p class="panel-url">www.keystoneaudit.co.nz</p>
    </div>
    <div class="front-details">
      <h1 class="person-name">Marcus Dellow</h1>
      <p class="person-role">Director / Structural Engineer</p>
      <p class="person-credentials">BEng(Hons), CPEng, CMengNZ, IntPE(NZ)</p>
    </div>
    <ul class="contact-list">
      <li>
        <svg viewBox="0 0 14 14"><rect x="3.5" y="0.5" width="7" height="13" rx="1.5" fill="none" stroke="#3a7fc9" stroke-width="1.4"/><circle cx="7" cy="11" r="0.9" fill="#3a7fc9"/></svg>
        0219364058
      </li>
      <li>
        <svg viewBox="0 0 14 14"><rect x="0.7" y="2.5" width="12.6" height="9" fill="#3a7fc9"/><path d="M0.7 2.5 L7 8 L13.3 2.5" fill="none" stroke="#f6f6f6" stroke-width="1.2"/></svg>
        marcus.dellow@keystoneaudit.co.nz
      </li>
      <li>
        <svg viewBox="0 0 14 14"><circle cx="7" cy="7" r="6.2" fill="#3a7fc9"/><ellipse cx="7" cy="7" rx="2.6" ry="6.2" fill="none" stroke="#f6f6f6" stroke-width="0.9"/><path d="M0.8 7 H13.2" stroke="#f6f6f6" stroke-width="0.9"/></svg>
        www.keystoneaudit.co.nz
      </li>
    </ul>
  </section>

  <section class="card card-back" aria-label="Card back">
    <div class="back-brand">
      <span class="brand-square"></span>
      <span class="back-name">Keystone Audit</span>
    </div>
  </section>
</main>
</body>
</html>
```